HR Technology Company (Corvixo) needs a consistent powerpoint deck for future presentations

We are Corvixo (corvixo-example.com). You can visit our website for colours scheme etc. I am looking for a full PPT pack which can be used for various presentations in the future. Sales Presentation, Company Overview etc. This must include charts, graphs, services (4/6/8 items), people slide, timeline slides etc among all the other common slides.

```html
<!DOCTYPE html>
<html lang="en">
<head>
<meta charset="utf-8">
<title>Corvixo Presentation Pack</title>
<link href="https://fonts.googleapis.com/css2?family=Open+Sans:wght@400;600;700;800&display=swap" rel="stylesheet">
<style>
:root{
  --orange:#f28c1c;
  --orange-deep:#e06a10;
  --amber:#f6a623;
  --gold:#d99a1a;
  --brown:#a8641c;
  --ink:#222;
  --muted:#8a8a8a;
  --line:#e6e6e6;
  --paper:#fff;
}
*{margin:0;padding:0;box-sizing:border-box}
html,body{width:1200px;height:1200px;overflow:hidden;background:#fff;font-family:"Open Sans",Arial,sans-serif}
.board{position:relative;width:1200px;height:1200px}
.slide{position:absolute;width:207px;height:116px;background:var(--paper);box-shadow:0 2px 7px rgba(0,0,0,.2);overflow:hidden}
.slide>*{position:absolute}
.mark{left:8px;top:7px;width:7px;height:7px;background:var(--orange)}
.logo{right:8px;top:6px;font-size:5px;font-weight:700;color:#333}
.logo.w{color:#fff}
.foot{left:8px;right:8px;bottom:3px;display:flex;justify-content:space-between;font-size:2px;color:#aaa}
.ttl{font-size:7px;font-weight:600;color:var(--ink);line-height:1.15}
.ttl span{color:var(--orange)}
.ttl.c{text-align:center;left:0;right:0}
.txt{font-size:2.3px;color:#777;line-height:1.45}
.txt.w{color:#fff}
.ph{background:linear-gradient(135deg,#c9a07c,#6d5646)}
.ph.o{background:linear-gradient(135deg,#f6b15a,#c9782a)}
.ph.d{background:linear-gradient(135deg,#5d6a78,#2f3640)}
.ph.l{background:linear-gradient(135deg,#e8d8c8,#a99582)}
.orng{background:var(--orange)}
.card{background:#fff;box-shadow:0 1px 3px rgba(0,0,0,.15);padding:3px;text-align:center}
.card b{display:block;font-size:2.6px;color:#333;margin:2px 0 1px}
.card.on{background:var(--orange)}
.card.on b,.card.on .txt{color:#fff}
.ic{display:block;margin:0 auto;width:6px;height:6px;border:1px solid var(--orange);border-radius:50%}
.card.on .ic{border-color:#fff}
.btn{background:var(--orange);color:#fff;font-size:2.2px;padding:1px 4px}
.big{font-weight:700;color:var(--orange)}
.dot{width:7px;height:7px;border-radius:50%}
.row{display:flex;gap:3px}
</style>
</head>
<body>
<div class="board">

<!-- row 1 -->
<div class="slide" style="left:31px;top:34px">
  <div class="logo" style="left:14px;right:auto;top:10px;font-size:6px">Corvixo</div>
  <div class="ph o" style="left:103px;top:0;width:104px;height:116px" role="img" aria-label="Office team meeting in warm light"></div>
  <div class="orng" style="left:14px;top:36px;width:88px;height:66px"></div>
  <div class="ttl" style="left:16px;top:45px;font-size:13px;font-weight:800">BUSINESS PLAN</div>
  <div class="txt w" style="left:17px;top:62px;width:40px">Lorem ipsum is simply dummy text of the printing and typesetting.</div>
  <div style="left:28px;top:84px;font-size:5px;color:#fff">Jan 26, 2023</div>
  <div class="txt w" style="left:28px;top:91px">Presented by Mara Lindqvist</div>
  <div class="foot"><span>Confidential - Not for Distribution</span><span></span></div>
</div>

<div class="slide" style="left:264px;top:34px">
  <div class="mark"></div><div class="logo">Corvixo</div>
  <div class="ttl" style="left:23px;top:22px">Today Agenda</div>
  <div class="ph o" style="left:20px;top:38px;width:187px;height:66px" role="img" aria-label="Team collaborating at a table, orange tint"></div>
  <div class="row" style="left:26px;top:48px;width:176px;gap:8px">
    <div style="flex:1"><div style="font-size:3px;color:#fff">Point 01</div><div class="txt w" style="margin-top:10px">Lorem ipsum dolor sit amet adipiscing elit.</div></div>
    <div style="flex:1"><div style="font-size:3px;color:#fff">Point 02</div><div class="txt w" style="margin-top:10px">Lorem ipsum dolor sit amet adipiscing elit.</div></div>
    <div style="flex:1"><div style="font-size:3px;color:#fff">Point 03</div><div class="txt w" style="margin-top:10px">Lorem ipsum dolor sit amet adipiscing elit.</div></div>
    <div style="flex:1"><div style="font-size:3px;color:#fff">Point 04</div><div class="txt w" style="margin-top:10px">Lorem ipsum dolor sit amet adipiscing elit.</div></div>
  </div>
  <div class="foot"><span>Confidential - Not for Distribution</span><span>www. corvixo-example.com</span></div>
</div>

<div class="slide" style="left:497px;top:34px">
  <div class="orng" style="left:0;top:0;width:207px;height:48px"></div>
  <div class="logo w">Corvixo</div>
  <div class="ttl c" style="top:20px;color:#fff">Welcome Messages</div>
  <div class="ph" style="left:89px;top:34px;width:28px;height:28px;border-radius:50%;border:2px solid #fff" role="img" aria-label="Portrait of the speaker"></div>
  <div style="left:0;right:0;top:66px;text-align:center;font-size:2.6px;color:#333">Mara Lindqvist</div>
  <div class="txt" style="left:28px;right:28px;top:75px;text-align:center">Lorem ipsum is simply dummy text of the printing and typesetting industry. Lorem ipsum has been the industry's standard dummy text ever since.</div>
  <div class="foot"><span>Confidential - Not for Distribution</span><span>www. corvixo-example.com</span></div>
</div>

<div class="slide" style="left:729px;top:34px">
  <div class="mark"></div><div class="logo">Corvixo</div>
  <div class="ttl" style="left:17px;top:26px;font-size:6.5px">Start With Our<br><span>Company Overview</span></div>
  <div class="txt" style="left:112px;top:26px;width:76px">Lorem ipsum is simply dummy text of the printing and typesetting industry standard.</div>
  <div class="ph l" style="left:0;top:56px;width:118px;height:40px" role="img" aria-label="Business handshake at a meeting"></div>
  <div class="orng" style="left:118px;top:56px;width:72px;height:40px"></div>
  <div class="txt w" style="left:123px;top:61px">Since</div>
  <div style="left:123px;top:66px;font-size:7px;color:#fff">2023</div>
  <div class="txt w" style="left:123px;top:76px;width:60px">Lorem ipsum is simply dummy text of the printing.</div>
  <div class="foot"><span>Confidential - Not for Distribution</span><span>www. corvixo-example.com</span></div>
</div>

<div class="slide" style="left:963px;top:34px">
  <div class="logo" style="left:16px;right:auto">Corvixo</div>
  <div class="ph" style="left:80px;top:0;width:127px;height:45px" role="img" aria-label="Colleagues working at laptops"></div>
  <div class="orng" style="left:140px;top:3px;width:64px;height:40px"></div>
  <div style="left:166px;top:8px;width:8px;height:8px;border:1px solid #fff;border-radius:50%"></div>
  <div class="txt w" style="left:146px;top:20px;width:54px;text-align:center">Lorem ipsum is simply dummy text of the printing.</div>
  <div class="card" style="left:17px;top:45px;width:125px;height:55px;text-align:left;padding:5px"></div>
  <div class="ttl" style="left:28px;top:55px;font-size:6px">Business <span>Plan Section</span></div>
  <div class="txt" style="left:28px;top:66px;width:108px">Lorem ipsum is simply dummy text of the printing and typesetting industry. Lorem ipsum has been the industry's standard dummy text ever since.</div>
  <div class="btn" style="left:90px;top:91px">Learn More</div>
  <div class="ph" style="left:138px;top:45px;width:60px;height:45px" role="img" aria-label="Woman typing on laptop"></div>
  <div class="foot"><span>Confidential - Not for Distribution</span><span>www. corvixo-example.com</span></div>
</div>

<!-- row 2 -->
<div class="slide" style="left:31px;top:179px">
  <div class="mark"></div><div class="logo">Corvixo</div>
  <div class="ttl c" style="top:20px">Objective <span>Marketing</span></div>
  <div class="card" style="left:31px;top:36px;width:94px;height:26px;text-align:left"><div class="txt">Lorem ipsum is simply dummy text of the printing and typesetting industry. Lorem ipsum has been the standard.</div></div>
  <div class="ph o" style="left:123px;top:36px;width:70px;height:26px" role="img" aria-label="Workspace with laptop"></div>
  <div style="left:160px;top:53px;font-size:5px;color:#333">+10.000</div>
  <div class="ph o" style="left:14px;top:68px;width:84px;height:28px" role="img" aria-label="Person working at desk"></div>
  <div style="left:21px;top:88px;font-size:5px;color:#333">0.51%</div>
  <div class="card" style="left:98px;top:68px;width:94px;height:28px;text-align:left"><div class="txt">Lorem ipsum is simply dummy text of the printing and typesetting industry. Lorem ipsum has been the standard.</div></div>
  <div class="foot"><span>Confidential - Not for Distribution</span><span>www. corvixo-example.com</span></div>
</div>

<div class="slide" style="left:264px;top:179px">
  <div class="mark"></div><div class="logo">Corvixo</div>
  <div style="left:0;top:55px;width:108px;height:61px;background:linear-gradient(135deg,#ee3b2b,#f59a2a)"></div>
  <div class="ph l" style="left:32px;top:22px;width:44px;height:76px" role="img" aria-label="Hands reviewing charts on a desk"></div>
  <div class="orng" style="left:32px;top:22px;width:44px;height:11px"></div>
  <div class="txt w" style="left:34px;top:26px">Marketing Target</div>
  <div class="ttl" style="left:92px;top:28px">Marketing Target<br><span style="font-size:5px">To Reach Our Successful</span></div>
  <div class="card" style="left:118px;top:58px;width:75px;height:8px"><div class="txt" style="color:#333">Simple Description dummy text</div></div>
  <div class="txt" style="left:118px;top:72px;width:75px">Lorem ipsum is simply dummy text of the printing and typesetting industry. Lorem ipsum has been the industry's standard dummy text ever since the 1500s.</div>
  <div class="foot"><span style="color:#fff">Confidential - Not for Distribution</span><span>www. corvixo-example.com</span></div>
</div>

<div class="slide" style="left:497px;top:179px">
  <div class="logo" style="left:16px;right:auto">Corvixo</div>
  <div class="mark" style="left:187px"></div>
  <div class="ttl" style="left:16px;top:30px">About Our<br>Statements</div>
  <div class="txt" style="left:16px;top:52px;width:62px">Lorem ipsum is simply dummy text of the printing and typesetting industry. Lorem ipsum has been the industry's standard dummy text ever since the 1500s.</div>
  <div class="btn" style="left:16px;top:91px">Read Detail</div>
  <div class="ph l" style="left:89px;top:22px;width:58px;height:36px" role="img" aria-label="Two women smiling at a laptop"></div>
  <div class="card" style="left:147px;top:22px;width:46px;height:36px;text-align:left"><div class="big" style="font-size:5px">70%</div><div class="txt">Lorem ipsum is simply dummy text of the printing.</div></div>
  <div class="orng" style="left:193px;top:19px;width:14px;height:42px"></div>
  <div class="ph d" style="left:99px;top:60px;width:65px;height:36px" role="img" aria-label="Engineer in safety gear in a tunnel"></div>
  <div class="foot"><span>Confidential - Not for Distribution</span><span>www. corvixo-example.com</span></div>
</div>

<div class="slide" style="left:729px;top:179px">
  <div class="mark"></div><div class="logo">Corvixo</div>
  <div class="ph l" style="left:14px;top:24px;width:68px;height:36px" role="img" aria-label="Team at a meeting table"></div>
  <div class="orng" style="left:14px;top:63px;width:48px;height:30px"></div>
  <div class="txt w" style="left:18px;top:70px;width:40px;font-style:italic">Lorem ipsum is simply dummy text of the printing and typesetting.</div>
  <div class="ph l" style="left:62px;top:63px;width:36px;height:30px" role="img" aria-label="Two colleagues talking"></div>
  <div class="ttl" style="left:92px;top:25px">About Talent<br><span>Mission Statements</span></div>
  <div class="txt" style="left:92px;top:48px;width:102px">Lorem ipsum is simply dummy text of the printing and typesetting industry. Lorem ipsum has been the industry's standard dummy text.</div>
  <div style="left:125px;top:71px;font-size:2.6px;color:#333">Mission Here :</div>
  <div class="txt" style="left:128px;top:76px;width:65px">• Lorem ipsum is simply dummy text<br>• Lorem ipsum is simply dummy<br>• Lorem ipsum is simply dummy text<br>• Lorem ipsum is simply dummy</div>
  <div class="foot"><span>Confidential - Not for Distribution</span><span>www. corvixo-example.com</span></div>
</div>

<div class="slide" style="left:963px;top:179px">
  <div class="logo" style="left:16px;right:auto">Corvixo</div>
  <div class="ph" style="left:120px;top:0;width:87px;height:62px" role="img" aria-label="Smiling woman working on laptop"></div>
  <div class="ttl" style="left:16px;top:26px">Product <span>&amp; Services</span></div>
  <div class="txt" style="left:16px;top:37px;width:98px">Lorem ipsum is simply dummy text of the printing and typesetting industry. Lorem ipsum has been the industry's standard dummy text ever since.</div>
  <div class="row" style="left:16px;top:63px;width:180px">
    <div class="card" style="flex:1;height:37px"><span class="ic"></span><b>Productions</b><div class="txt">Lorem ipsum is simply dummy text.</div></div>
    <div class="card on" style="flex:1;height:37px"><span class="ic"></span><b>Business Services</b><div class="txt">Lorem ipsum is simply dummy text.</div></div>
    <div class="card" style="flex:1;height:37px"><span class="ic"></span><b>Productions</b><div class="txt">Lorem ipsum is simply dummy text.</div></div>
    <div class="card" style="flex:1;height:37px"><span class="ic"></span><b>Business Services</b><div class="txt">Lorem ipsum is simply dummy text.</div></div>
  </div>
  <div class="foot"><span>Confidential - Not for Distribution</span><span>www. corvixo-example.com</span></div>
</div>

<!-- row 3 -->
<div class="slide" style="left:31px;top:324px">
  <div class="ph" style="left:0;top:0;width:207px;height:55px" role="img" aria-label="Team working in a bright office"></div>
  <div class="ttl" style="left:16px;top:7px;color:#fff">Product <span>&amp; Services</span></div>
  <div class="row" style="left:16px;top:20px;width:176px;flex-wrap:wrap">
    <div class="card" style="width:41px;height:41px"><span class="ic"></span><b>Productions</b><div class="txt">Lorem ipsum is simply dummy text.</div></div>
    <div class="card on" style="width:41px;height:41px"><span class="ic"></span><b>Business Services</b><div class="txt">Lorem ipsum is simply dummy text.</div></div>
    <div class="card" style="width:41px;height:41px"><span class="ic"></span><b>Productions</b><div class="txt">Lorem ipsum is simply dummy text.</div></div>
    <div class="card" style="width:41px;height:41px"><span class="ic"></span><b>Business Services</b><div class="txt">Lorem ipsum is simply dummy text.</div></div>
    <div class="card" style="width:41px;height:41px"><span class="ic"></span><b>Productions</b><div class="txt">Lorem ipsum is simply dummy text.</div></div>
    <div class="card" style="width:41px;height:41px"><span class="ic"></span><b>Business Services</b><div class="txt">Lorem ipsum is simply dummy text.</div></div>
    <div class="card" style="width:41px;height:41px"><span class="ic"></span><b>Productions</b><div class="txt">Lorem ipsum is simply dummy text.</div></div>
    <div class="card on" style="width:41px;height:41px"><span class="ic"></span><b>Business Services</b><div class="txt">Lorem ipsum is simply dummy text.</div></div>
  </div>
  <div class="foot"><span>Confidential - Not for Distribution</span><span>www. corvixo-example.com</span></div>
</div>

<div class="slide" style="left:264px;top:324px">
  <div class="mark"></div><div class="logo">Corvixo</div>
  <div class="ttl" style="left:26px;top:26px">Our Product<br><span>Marketing Line</span></div>
  <div class="txt" style="left:98px;top:27px;width:92px">Lorem ipsum is simply dummy text of the printing and typesetting industry. Lorem ipsum has been the industry's standard dummy text.</div>
  <div class="orng" style="left:0;top:73px;width:26px;height:43px"></div>
  <div class="ph" style="left:26px;top:55px;width:88px;height:41px" role="img" aria-label="Team presentation in a meeting room"></div>
  <div class="ph d" style="left:114px;top:55px;width:93px;height:41px" role="img" aria-label="Content studio workspace"></div>
  <div class="foot"><span style="color:#fff">Confidential - Not for Distribution</span><span>www. corvixo-example.com</span></div>
</div>

<div class="slide" style="left:497px;top:324px">
  <div class="mark"></div><div class="logo">Corvixo</div>
  <div class="ph o" style="left:20px;top:32px;width:42px;height:70px" role="img" aria-label="Person reading documents"></div>
  <div style="left:25px;top:70px;font-size:4px;color:#fff">+152</div>
  <div class="card" style="left:67px;top:22px;width:40px;height:62px"><span class="ic" style="margin-top:8px"></span><b>Option Here</b><div class="txt">Lorem ipsum is simply dummy text of the printing.</div><span class="btn" style="display:inline-block;margin-top:4px">Read Detail</span></div>
  <div class="ttl" style="left:120px;top:28px">Competitive<br><span>Thinking<br>Innovation</span></div>
  <div class="txt" style="left:120px;top:62px;width:70px">Lorem ipsum is simply dummy text of the printing and typesetting industry. Lorem ipsum has been the standard.</div>
  <div class="foot"><span>Confidential - Not for Distribution</span><span>www. corvixo-example.com</span></div>
</div>

<div class="slide" style="left:729px;top:324px">
  <div class="logo" style="left:16px;right:auto">Corvixo</div>
  <div class="ph o" style="left:157px;top:0;width:50px;height:116px" role="img" aria-label="Professional at work, orange tint"></div>
  <div class="ttl" style="left:17px;top:30px">Meet Our<br>Professional</div>
  <div class="txt" style="left:17px;top:52px;width:76px">Lorem ipsum is simply dummy text of the printing and typesetting industry. Lorem ipsum has been the industry's standard dummy text ever since the 1500s, when an unknown printer took a galley of type.</div>
  <div class="card" style="left:105px;top:16px;width:62px;height:25px;text-align:left;padding-left:20px"><b>Ivy Harlan</b><div class="txt">Lorem ipsum is simply dummy text.</div></div>
  <div class="card on" style="left:105px;top:46px;width:62px;height:25px;text-align:left;padding-left:20px"><b>Elena Voss</b><div class="txt">Lorem ipsum is simply dummy text.</div></div>
  <div class="card" style="left:105px;top:76px;width:62px;height:25px;text-align:left;padding-left:20px"><b>Tom Reyes</b><div class="txt">Lorem ipsum is simply dummy text.</div></div>
  <div class="ph l" style="left:108px;top:20px;width:14px;height:14px;border-radius:50%" role="img" aria-label="Team member portrait"></div>
  <div class="ph l" style="left:108px;top:50px;width:14px;height:14px;border-radius:50%" role="img" aria-label="Team member portrait"></div>
  <div class="ph l" style="left:108px;top:80px;width:14px;height:14px;border-radius:50%" role="img" aria-label="Team member portrait"></div>
  <div class="foot"><span>Confidential - Not for Distribution</span><span style="color:#fff">www. corvixo-example.com</span></div>
</div>

<div class="slide" style="left:963px;top:324px">
  <div class="logo">Corvixo</div>
  <div class="orng" style="left:0;top:0;width:30px;height:116px"></div>
  <div class="mark" style="left:20px;top:10px;background:#f7b366"></div>
  <div class="card" style="left:24px;top:26px;width:46px;height:62px;text-align:left;padding:0"></div>
  <div class="ph" style="left:24px;top:26px;width:46px;height:28px" role="img" aria-label="Team member at desk"></div>
  <div style="left:27px;top:57px"><b style="font-size:2.6px;color:#333">Elena Voss</b><div class="txt" style="width:40px">Lorem ipsum is simply dummy text of the printing.</div></div>
  <div class="card" style="left:72px;top:26px;width:46px;height:62px;padding:0"></div>
  <div class="ph d" style="left:72px;top:26px;width:46px;height:28px" role="img" aria-label="Team member at desk"></div>
  <div style="left:75px;top:57px"><b style="font-size:2.6px;color:#333">Tom Reyes</b><div class="txt" style="width:40px">Lorem ipsum is simply dummy text of the printing.</div></div>
  <div class="ttl" style="left:126px;top:29px">Our Market<br><span>Team</span></div>
  <div class="txt" style="left:126px;top:47px;width:66px">Lorem ipsum is simply dummy text of the printing and typesetting industry. Lorem ipsum has been the industry's standard dummy text ever since the 1500s.</div>
  <div class="foot"><span style="color:#fff">Confidential - Not for Distribution</span><span>www. corvixo-example.com</span></div>
</div>

<!-- row 4 -->
<div class="slide" style="left:31px;top:470px">
  <div class="logo">Corvixo</div>
  <div class="orng" style="left:0;top:0;width:44px;height:116px"></div>
  <div class="ttl" style="left:68px;top:9px">Our Market <span>Team</span></div>
  <div class="card" style="left:22px;top:26px;width:44px;height:64px;padding:0"></div>
  <div class="ph" style="left:22px;top:26px;width:44px;height:28px" role="img" aria-label="Team member portrait"></div>
  <div style="left:25px;top:56px"><b style="font-size:2.6px;color:#333">Elena Voss</b><div class="txt" style="width:38px">Lorem ipsum is simply dummy text.</div></div>
  <div class="card" style="left:70px;top:26px;width:44px;height:64px;padding:0"></div>
  <div class="ph" style="left:70px;top:26px;width:44px;height:28px" role="img" aria-label="Team member portrait"></div>
  <div style="left:73px;top:56px"><b style="font-size:2.6px;color:#333">Elena Voss</b><div class="txt" style="width:38px">Lorem ipsum is simply dummy text.</div></div>
  <div class="card" style="left:118px;top:26px;width:44px;height:64px;padding:0"></div>
  <div class="ph d" style="left:118px;top:26px;width:44px;height:28px" role="img" aria-label="Team member portrait"></div>
  <div style="left:121px;top:56px"><b style="font-size:2.6px;color:#333">Tom Reyes</b><div class="txt" style="width:38px">Lorem ipsum is simply dummy text.</div></div>
  <div class="txt" style="left:168px;top:26px;width:28px">Lorem ipsum is simply dummy text of the printing and typesetting industry standard.</div>
  <div class="foot"><span style="color:#fff">Confidential - Not for Distribution</span><span>www. corvixo-example.com</span></div>
</div>

<div class="slide" style="left:264px;top:470px">
  <div class="logo">Corvixo</div>
  <div class="ph o" style="left:20px;top:0;width:88px;height:116px" role="img" aria-label="Smiling woman, orange tone"></div>
  <div class="ttl" style="left:101px;top:30px">Our Product<br><span>Marketing Line</span></div>
  <div class="txt" style="left:101px;top:52px;width:92px">Lorem ipsum is simply dummy text of the printing and typesetting industry. Lorem ipsum has been the industry's standard dummy text ever since the 1500s, when an unknown printer took a galley.</div>
  <div class="foot"><span style="color:#fff">Confidential - Not for Distribution</span><span>www. corvixo-example.com</span></div>
</div>

<div class="slide" style="left:497px;top:470px">
  <div class="logo" style="left:16px;right:auto">Corvixo</div>
  <div class="ttl" style="left:16px;top:24px">Our Product <span>Marketing Line</span></div>
  <div class="txt" style="left:16px;top:34px;width:100px">Lorem ipsum is simply dummy text of the printing and typesetting industry. Lorem ipsum has been the industry's standard dummy text.</div>
  <div class="ph" style="left:14px;top:60px;width:42px;height:38px" role="img" aria-label="Team in a workshop"></div>
  <div class="ph l" style="left:58px;top:60px;width:56px;height:38px" role="img" aria-label="Colleagues at a shared table"></div>
  <div class="ph d" style="left:122px;top:0;width:68px;height:98px" role="img" aria-label="Team hands stacked together"></div>
  <div class="foot"><span>Confidential - Not for Distribution</span><span>www. corvixo-example.com</span></div>
</div>

<div class="slide" style="left:729px;top:470px">
  <div class="logo" style="left:16px;right:auto">Corvixo</div>
  <div class="mark" style="left:184px;top:10px"></div>
  <div class="ttl" style="left:14px;top:26px">Our Market<br><span>Growth Here</span></div>
  <div class="txt" style="left:18px;top:50px;width:78px"><b style="color:#333">First Aspects</b><br>• Lorem ipsum is simply dummy text<br>• Lorem ipsum is simply dummy text<br>• Lorem ipsum is simply dummy<br><br><b style="color:#333">Second Aspects</b><br>• Lorem ipsum is simply dummy text<br>• Lorem ipsum is simply dummy</div>
  <div class="ph" style="left:103px;top:0;width:67px;height:55px" role="img" aria-label="Smiling man with beard"></div>
  <div class="ph l" style="left:103px;top:62px;width:67px;height:36px" role="img" aria-label="Team meeting around a table"></div>
  <div class="foot"><span>Confidential - Not for Distribution</span><span>www. corvixo-example.com</span></div>
</div>

<div class="slide" style="left:963px;top:470px">
  <div class="logo">Corvixo</div>
  <div class="ph d" style="left:20px;top:0;width:86px;height:74px" role="img" aria-label="Worker in safety suit in a tunnel"></div>
  <div class="ttl" style="left:118px;top:27px">About Sales<br><span>Forcasting</span></div>
  <div class="txt" style="left:118px;top:47px;width:76px">Lorem ipsum is simply dummy text of the printing and typesetting industry. Lorem ipsum has been the standard.</div>
  <div class="card on" style="left:15px;top:72px;width:58px;height:26px;text-align:left;padding-left:14px"><b>Simple Description</b><div class="txt">Lorem ipsum is simply dummy text.</div></div>
  <div class="card" style="left:78px;top:72px;width:58px;height:26px;text-align:left;padding-left:14px"><b>Simple Description</b><div class="txt">Lorem ipsum is simply dummy text.</div></div>
  <div class="card" style="left:141px;top:72px;width:58px;height:26px;text-align:left;padding-left:14px"><b>Simple Description</b><div class="txt">Lorem ipsum is simply dummy text.</div></div>
  <div class="dot orng" style="left:18px;top:76px;border:1px solid #fff"></div>
  <div class="dot orng" style="left:81px;top:76px"></div>
  <div class="dot orng" style="left:144px;top:76px"></div>
  <div class="foot"><span>Confidential - Not for Distribution</span><span>www. corvixo-example.com</span></div>
</div>

<!-- row 5 -->
<div class="slide" style="left:31px;top:614px">
  <div class="logo">Corvixo</div>
  <div class="ph" style="left:20px;top:0;width:44px;height:84px" role="img" aria-label="Woman in a business setting"></div>
  <div class="ph l" style="left:66px;top:10px;width:44px;height:106px" role="img" aria-label="Woman smiling at work"></div>
  <div class="orng" style="left:0;top:78px;width:78px;height:26px"></div>
  <div class="txt w" style="left:22px;top:84px;width:52px"><b>Market Aspects</b><br>Lorem ipsum is simply dummy text of the printing.</div>
  <div class="ttl" style="left:123px;top:22px">Our Business<br><span>Opportunities</span></div>
  <div class="dot" style="left:123px;top:44px;background:#222"></div>
  <div class="txt" style="left:134px;top:43px;width:62px"><b style="color:#333">Subtitle here</b><br>A peep at some distant orb has power to raise.</div>
  <div class="dot orng" style="left:123px;top:64px"></div>
  <div class="txt" style="left:134px;top:63px;width:62px"><b style="color:var(--orange)">Subtitle here</b><br>A peep at some distant orb has power to raise.</div>
  <div class="dot" style="left:123px;top:84px;background:#999"></div>
  <div class="txt" style="left:134px;top:83px;width:62px"><b style="color:#666">Subtitle here</b><br>A peep at some distant orb has power to raise.</div>
  <div class="foot"><span>Confidential - Not for Distribution</span><span>www. corvixo-example.com</span></div>
</div>

<div class="slide" style="left:264px;top:614px">
  <div class="logo" style="left:18px;right:auto">Corvixo</div>
  <div class="ph l" style="left:88px;top:0;width:119px;height:116px" role="img" aria-label="Woman working at a computer in an office"></div>
  <div class="orng" style="left:22px;top:32px;width:86px;height:26px"></div>
  <div style="left:35px;top:38px;font-size:11px;color:#fff;font-weight:600">Break Slide</div>
  <div class="orng" style="left:42px;top:60px;width:75px;height:20px;background:var(--amber)"></div>
  <div class="txt w" style="left:48px;top:64px;width:64px"><b>Business Plan Presentation</b><br>Lorem ipsum is simply dummy text of the printing.</div>
  <div class="foot"><span>Confidential - Not for Distribution</span><span></span></div>
</div>

<div class="slide" style="left:497px;top:614px">
  <div class="mark"></div><div class="logo">Corvixo</div>
  <div class="ttl" style="left:16px;top:31px">What <span>we do</span></div>
  <div class="txt" style="left:16px;top:46px;width:70px">Lorem ipsum is simply dummy text of the printing and typesetting industry. Lorem ipsum has been the industry's standard dummy text ever since the 1500s, when an unknown printer took a galley of type and scrambled it to make a type specimen book.</div>
  <div class="dot" style="left:99px;top:27px;background:#222;width:9px;height:9px"></div>
  <div class="txt" style="left:112px;top:27px;width:80px"><b style="color:#333">Subtitle here</b><br>A peep at some distant orb has power to raise and purify.</div>
  <div class="dot orng" style="left:99px;top:47px;width:9px;height:9px"></div>
  <div class="txt" style="left:112px;top:47px;width:80px"><b style="color:var(--orange)">Subtitle here</b><br>A peep at some distant orb has power to raise and purify.</div>
  <div class="dot" style="left:99px;top:67px;background:#999;width:9px;height:9px"></div>
  <div class="txt" style="left:112px;top:67px;width:80px"><b style="color:#666">Subtitle here</b><br>A peep at some distant orb has power to raise and purify.</div>
  <div class="dot" style="left:99px;top:87px;background:#999;width:9px;height:9px"></div>
  <div class="txt" style="left:112px;top:87px;width:80px"><b style="color:#666">Subtitle here</b><br>A peep at some distant orb has power to raise and purify.</div>
  <div class="foot"><span>Confidential - Not for Distribution</span><span>www. corvixo-example.com</span></div>
</div>

<div class="slide" style="left:729px;top:614px">
  <div class="mark"></div><div class="logo">Corvixo</div>
  <div class="ttl c" style="top:7px;font-size:6.5px">What people <span>say about Us</span></div>
  <div class="orng" style="left:22px;top:36px;width:44px;height:26px;border-radius:50%"></div>
  <div class="orng" style="left:80px;top:36px;width:44px;height:26px;border-radius:50%"></div>
  <div class="orng" style="left:137px;top:36px;width:44px;height:26px;border-radius:50%"></div>
  <div class="txt w" style="left:27px;top:42px;width:34px;text-align:center">Lorem ipsum is simply dummy text of the printing.</div>
  <div class="txt w" style="left:85px;top:42px;width:34px;text-align:center">Lorem ipsum is simply dummy text of the printing.</div>
  <div class="txt w" style="left:142px;top:42px;width:34px;text-align:center">Lorem ipsum is simply dummy text of the printing.</div>
  <div class="ph d" style="left:22px;top:68px;width:10px;height:10px;border-radius:50%" role="img" aria-label="Client portrait"></div>
  <div class="ph d" style="left:80px;top:68px;width:10px;height:10px;border-radius:50%" role="img" aria-label="Client portrait"></div>
  <div class="ph d" style="left:137px;top:68px;width:10px;height:10px;border-radius:50%" role="img" aria-label="Client portrait"></div>
  <div class="txt" style="left:35px;top:70px"><b style="color:#333">Name Surname</b><br><span style="color:var(--orange)">Position</span></div>
  <div class="txt" style="left:93px;top:70px"><b style="color:#333">Name Surname</b><br><span style="color:var(--orange)">Position</span></div>
  <div class="txt" style="left:150px;top:70px"><b style="color:#333">Name Surname</b><br><span style="color:var(--orange)">Position</span></div>
  <div class="foot"><span>Confidential - Not for Distribution</span><span>www. corvixo-example.com</span></div>
</div>

<div class="slide" style="left:963px;top:614px">
  <div class="mark"></div><div class="logo">Corvixo</div>
  <div class="ttl" style="left:17px;top:33px">Our 4 <span>Services</span></div>
  <div class="txt" style="left:17px;top:45px;width:96px"><b style="color:#333">Subtitle</b><br>Lorem ipsum is simply dummy text of the printing and typesetting industry. Lorem ipsum has been the industry's standard dummy text ever since the 1500s, when an unknown printer took a galley of type and scrambled it to make a type specimen book.</div>
  <div class="card" style="left:113px;top:26px;width:36px;height:36px;border-top:1px solid var(--orange)"><span class="ic" style="margin-top:4px"></span><b>Subtitle here</b><div class="txt">Be a drain of sacred music.</div></div>
  <div class="card" style="left:152px;top:26px;width:36px;height:36px"><span class="ic" style="margin-top:4px"></span><b>Subtitle here</b><div class="txt">Be a drain of sacred music.</div></div>
  <div class="card" style="left:113px;top:64px;width:36px;height:36px"><span class="ic" style="margin-top:4px"></span><b>Subtitle here</b><div class="txt">Be a drain of sacred music.</div></div>
  <div class="card" style="left:152px;top:64px;width:36px;height:36px"><span class="ic" style="margin-top:4px"></span><b>Subtitle here</b><div class="txt">Be a drain of sacred music.</div></div>
  <div class="foot"><span>Confidential - Not for Distribution</span><span>www. corvixo-example.com</span></div>
</div>

<!-- row 6 -->
<div class="slide" style="left:31px;top:759px">
  <div class="mark"></div><div class="logo">Corvixo</div>
  <div class="ttl" style="left:17px;top:34px">Our 6 <span>Services</span></div>
  <div class="txt" style="left:17px;top:46px;width:56px">Lorem ipsum is simply dummy text of the printing and typesetting industry. Lorem ipsum has been the industry's standard dummy text ever since the 1500s.</div>
  <div class="row" style="left:84px;top:27px;width:108px;flex-wrap:wrap">
    <div class="card" style="width:34px;height:36px;border-top:1px solid var(--orange)"><span class="ic" style="margin-top:4px"></span><b>Subtitle here</b><div class="txt">Be a drain of sacred music.</div></div>
    <div class="card" style="width:34px;height:36px"><span class="ic" style="margin-top:4px"></span><b>Subtitle here</b><div class="txt">Be a drain of sacred music.</div></div>
    <div class="card" style="width:34px;height:36px"><span class="ic" style="margin-top:4px"></span><b>Subtitle here</b><div class="txt">Be a drain of sacred music.</div></div>
    <div class="card" style="width:34px;height:36px"><span class="ic" style="margin-top:4px"></span><b>Subtitle here</b><div class="txt">Be a drain of sacred music.</div></div>
    <div class="card" style="width:34px;height:36px"><span class="ic" style="margin-top:4px"></span><b>Subtitle here</b><div class="txt">Be a drain of sacred music.</div></div>
    <div class="card" style="width:34px;height:36px"><span class="ic" style="margin-top:4px"></span><b>Subtitle here</b><div class="txt">Be a drain of sacred music.</div></div>
  </div>
  <div class="foot"><span>Confidential - Not for Distribution</span><span>www. corvixo-example.com</span></div>
</div>

<div class="slide" style="left:264px;top:759px">
  <div class="mark"></div><div class="logo">Corvixo</div>
  <div class="ttl" style="left:15px;top:37px">Our 8<br><span>Services</span></div>
  <div class="txt" style="left:15px;top:60px;width:38px">Lorem ipsum is simply dummy text of the printing and typesetting industry standard.</div>
  <div class="row" style="left:54px;top:30px;width:144px;flex-wrap:wrap">
    <div class="card" style="width:33px;height:35px;border-top:1px solid var(--orange)"><span class="ic" style="margin-top:4px"></span><b>Subtitle here</b><div class="txt">Be a drain of music.</div></div>
    <div class="card" style="width:33px;height:35px"><span class="ic" style="margin-top:4px"></span><b>Subtitle here</b><div class="txt">Be a drain of music.</div></div>
    <div class="card" style="width:33px;height:35px"><span class="ic" style="margin-top:4px"></span><b>Subtitle here</b><div class="txt">Be a drain of music.</div></div>
    <div class="card" style="width:33px;height:35px"><span class="ic" style="margin-top:4px"></span><b>Subtitle here</b><div class="txt">Be a drain of music.</div></div>
    <div class="card" style="width:33px;height:35px"><span class="ic" style="margin-top:4px"></span><b>Subtitle here</b><div class="txt">Be a drain of music.</div></div>
    <div class="card" style="width:33px;height:35px"><span class="ic" style="margin-top:4px"></span><b>Subtitle here</b><div class="txt">Be a drain of music.</div></div>
    <div class="card" style="width:33px;height:35px"><span class="ic" style="margin-top:4px"></span><b>Subtitle here</b><div class="txt">Be a drain of music.</div></div>
    <div class="card" style="width:33px;height:35px"><span class="ic" style="margin-top:4px"></span><b>Subtitle here</b><div class="txt">Be a drain of music.</div></div>
  </div>
  <div class="foot"><span>Confidential - Not for Distribution</span><span>www. corvixo-example.com</span></div>
</div>

<div class="slide" style="left:497px;top:759px">
  <div class="mark"></div><div class="logo">Corvixo</div>
  <div class="ttl c" style="top:19px">Your Title <span>Text Goes Here</span></div>
  <svg style="left:0;top:40px" width="207" height="52" viewBox="0 0 207 52">
    <path d="M0 26 Q12 6 24 26 T48 26 T72 26 T96 26 T120 26 T144 26 T168 26 T192 26 T216 26" fill="none" stroke="#e2e2e2" stroke-width="2"/>
    <g fill="#fff" stroke="#f28c1c" stroke-width="1.4">
      <circle cx="58" cy="26" r="9"/><circle cx="88" cy="26" r="9"/><circle cx="118" cy="26" r="9"/><circle cx="148" cy="26" r="9"/>
    </g>
    <g fill="#f28c1c"><rect x="55" y="23" width="6" height="6"/><rect x="85" y="23" width="6" height="6"/><rect x="115" y="23" width="6" height="6"/><rect x="145" y="23" width="6" height="6"/></g>
  </svg>
  <div class="txt" style="left:46px;top:37px;text-align:center"><b style="color:#333">Feature title one</b><br>Lorem ipsum dolor sit.</div>
  <div class="txt" style="left:106px;top:37px;text-align:center"><b style="color:#333">Feature title one</b><br>Lorem ipsum dolor sit.</div>
  <div class="txt" style="left:76px;top:84px;text-align:center"><b style="color:#333">Feature title one</b><br>Lorem ipsum dolor sit.</div>
  <div class="txt" style="left:136px;top:84px;text-align:center"><b style="color:#333">Feature title one</b><br>Lorem ipsum dolor sit.</div>
  <div class="foot"><span>Confidential - Not for Distribution</span><span>www. corvixo-example.com</span></div>
</div>

<div class="slide" style="left:729px;top:759px">
  <div class="mark"></div><div class="logo">Corvixo</div>
  <div class="ttl c" style="top:25px">Your Title <span>Text Goes Here</span></div>
  <div class="txt" style="left:28px;top:42px;text-align:center;width:30px"><b style="color:#333">Amazing history</b><br>content</div>
  <div class="txt" style="left:88px;top:42px;text-align:center;width:30px"><b style="color:#333">Amazing history</b><br>content</div>
  <div class="txt" style="left:148px;top:42px;text-align:center;width:30px"><b style="color:#333">Amazing history</b><br>content</div>
  <svg style="left:10px;top:53px" width="187" height="30" viewBox="0 0 187 30">
    <g fill="#fff" stroke-width="2.5">
      <circle cx="18" cy="15" r="12" stroke="#f6a623"/><circle cx="48" cy="15" r="12" stroke="#f28c1c"/>
      <circle cx="78" cy="15" r="12" stroke="#f6a623"/><circle cx="108" cy="15" r="12" stroke="#e07a1c"/>
      <circle cx="138" cy="15" r="12" stroke="#a8641c"/><circle cx="168" cy="15" r="12" stroke="#f28c1c"/>
    </g>
    <g font-size="5" fill="#f28c1c" text-anchor="middle" font-family="Open Sans,sans-serif">
      <text x="18" y="17">1992</text><text x="48" y="17">1995</text><text x="78" y="17">2000</text>
      <text x="108" y="17">2007</text><text x="138" y="17">2016</text><text x="168" y="17">2022</text>
    </g>
  </svg>
  <div class="txt" style="left:58px;top:85px;text-align:center;width:30px"><b style="color:#333">Amazing history</b><br>content</div>
  <div class="txt" style="left:118px;top:85px;text-align:center;width:30px"><b style="color:#333">Amazing history</b><br>content</div>
  <div class="txt" style="left:168px;top:85px;text-align:center;width:30px"><b style="color:#333">Amazing history</b><br>content</div>
  <div class="foot"><span>Confidential - Not for Distribution</span><span>www. corvixo-example.com</span></div>
</div>

<div class="slide" style="left:963px;top:759px">
  <div class="mark"></div><div class="logo">Corvixo</div>
  <div class="ttl c" style="top:17px">Your Title <span>Text Goes Here</span></div>
  <svg style="left:64px;top:32px" width="80" height="66" viewBox="0 0 80 66">
    <polygon points="40,2 48,12 32,12" fill="#f6a623"/>
    <polygon points="31,14 49,14 55,26 25,26" fill="#f28c1c"/>
    <polygon points="24,28 56,28 62,40 18,40" fill="#d99a1a"/>
    <polygon points="17,42 63,42 69,54 11,54" fill="#f6a623"/>
    <polygon points="10,56 70,56 76,64 4,64" fill="#c97a3a"/>
  </svg>
  <div class="txt" style="left:30px;top:36px;text-align:right;width:30px"><b style="color:#333">Option One</b><br>Lorem ipsum dolor.</div>
  <div class="txt" style="left:22px;top:59px;text-align:right;width:30px"><b style="color:#333">Option Three</b><br>Lorem ipsum dolor.</div>
  <div class="txt" style="left:16px;top:82px;text-align:right;width:30px"><b style="color:#333">Option Five</b><br>Lorem ipsum dolor.</div>
  <div class="txt" style="left:146px;top:46px;width:34px"><b style="color:#333">Option Two</b><br>Lorem ipsum dolor.</div>
  <div class="txt" style="left:160px;top:70px;width:34px"><b style="color:#333">Option Four</b><br>Lorem ipsum dolor.</div>
  <div class="foot"><span>Confidential - Not for Distribution</span><span>www. corvixo-example.com</span></div>
</div>

<!-- row 7 -->
<div class="slide" style="left:31px;top:904px">
  <div class="mark"></div><div class="logo">Corvixo</div>
  <div class="ttl c" style="top:20px">Your Title <span>Text Goes Here</span></div>
  <svg style="left:76px;top:40px" width="54" height="54" viewBox="0 0 54 54" font-family="Open Sans,sans-serif" font-size="15" font-weight="600" text-anchor="middle">
    <rect x="0" y="0" width="25" height="25" rx="7" fill="#f28c1c"/><rect x="28" y="0" width="25" height="25" rx="7" fill="#f6a623"/>
    <rect x="0" y="28" width="25" height="25" rx="7" fill="#f6a623"/><rect x="28" y="28" width="25" height="25" rx="7" fill="#f28c1c"/>
    <g fill="#fff"><text x="12.5" y="18">S</text><text x="40.5" y="18">W</text><text x="12.5" y="46">T</text><text x="40.5" y="46">O</text></g>
  </svg>
  <div class="txt" style="left:22px;top:44px;width:50px;text-align:right"><b style="color:var(--orange)">Strength</b><br>A wonderful serenity has taken possession of my entire soul.</div>
  <div class="txt" style="left:22px;top:74px;width:50px;text-align:right"><b style="color:var(--orange)">Opportunity</b><br>A wonderful serenity has taken possession of my entire soul.</div>
  <div class="txt" style="left:136px;top:44px;width:50px"><b style="color:var(--orange)">Weakness</b><br>A wonderful serenity has taken possession of my entire soul.</div>
  <div class="txt" style="left:136px;top:74px;width:50px"><b style="color:var(--orange)">Threats</b><br>A wonderful serenity has taken possession of my entire soul.</div>
  <div class="foot"><span>Confidential - Not for Distribution</span><span>www. corvixo-example.com</span></div>
</div>

<div class="slide" style="left:264px;top:904px">
  <div class="mark"></div><div class="logo">Corvixo</div>
  <div class="ttl" style="left:24px;top:25px">Your Title Text<br><span>Goes Here</span></div>
  <div class="txt" style="left:24px;top:46px;width:70px">Lorem ipsum dolor sit amet, consectetur adipiscing elit.</div>
  <div class="card" style="left:24px;top:56px;width:70px;height:34px;padding:4px">
    <div class="row" style="justify-content:space-around"><span class="big" style="font-size:5px">70,5%</span><span class="big" style="font-size:5px">80,5%</span></div>
    <div class="row" style="justify-content:space-around;margin-top:9px"><span class="big" style="font-size:5px">80,5%</span><span class="big" style="font-size:5px">90,0%</span></div>
  </div>
  <svg style="left:104px;top:22px" width="96" height="82" viewBox="0 0 96 82">
    <polygon points="48,2 6,58 48,80" fill="#f6a623"/>
    <polygon points="48,2 90,58 48,80" fill="#d99a1a"/>
    <line x1="22" y1="38" x2="74" y2="38" stroke="#fff" stroke-width="1"/>
    <line x1="35" y1="20" x2="61" y2="20" stroke="#fff" stroke-width="1"/>
    <g fill="#f28c1c" stroke="#fff" stroke-width="1"><circle cx="48" cy="15" r="5"/><circle cx="28" cy="50" r="6"/><circle cx="52" cy="60" r="7"/><circle cx="72" cy="32" r="5"/></g>
  </svg>
  <div class="foot"><span>Confidential - Not for Distribution</span><span>www. corvixo-example.com</span></div>
</div>

<div class="slide" style="left:497px;top:904px">
  <div class="mark"></div><div class="logo">Corvixo</div>
  <div class="ttl c" style="top:20px">Your Title <span>Text Goes Here</span></div>
  <div class="txt" style="left:60px;top:34px;width:50px"><b style="color:#333">▸ Teamwork</b><br>Lorem ipsum dolor sit amet, consectetur.</div>
  <div class="txt" style="left:130px;top:34px;width:50px"><b style="color:#333">▸ Setting</b><br>Lorem ipsum dolor sit amet, consectetur.</div>
  <div style="left:10px;top:53px;width:187px;height:14px;border-radius:7px;background:#efefef"></div>
  <div class="row" style="left:20px;top:56px;width:170px;gap:2px">
    <div class="orng" style="flex:1;height:8px;font-size:2.4px;color:#fff;text-align:center;line-height:8px">Your text here</div>
    <div class="orng" style="flex:1;height:8px;font-size:2.4px;color:#fff;text-align:center;line-height:8px">Your text here</div>
    <div class="orng" style="flex:1;height:8px;font-size:2.4px;color:#fff;text-align:center;line-height:8px">Your text here</div>
    <div class="orng" style="flex:1;height:8px;font-size:2.4px;color:#fff;text-align:center;line-height:8px">Your text here</div>
  </div>
  <div class="txt" style="left:30px;top:76px;width:50px"><b style="color:#333">▸ Ideas</b><br>Lorem ipsum dolor sit amet, consectetur.</div>
  <div class="txt" style="left:104px;top:76px;width:50px"><b style="color:#333">▸ GearHead</b><br>Lorem ipsum dolor sit amet, consectetur.</div>
  <div class="foot"><span>Confidential - Not for Distribution</span><span>www. corvixo-example.com</span></div>
</div>

<div class="slide" style="left:729px;top:904px">
  <div class="mark"></div><div class="logo">Corvixo</div>
  <svg style="left:68px;top:18px" width="70" height="84" viewBox="0 0 70 84">
    <path d="M12 40 A24 24 0 0 1 58 30" fill="none" stroke="#f28c1c" stroke-width="9"/>
    <polygon points="52,20 68,30 52,40" fill="#f28c1c"/>
    <path d="M58 46 A24 24 0 0 1 12 54" fill="none" stroke="#d99a1a" stroke-width="9"/>
    <polygon points="18,64 2,54 18,44" fill="#d99a1a"/>
    <circle cx="35" cy="42" r="14" fill="#fff" stroke="#eee"/>
    <text x="35" y="45" font-size="7" text-anchor="middle" font-family="Open Sans,sans-serif" fill="#222">2023</text>
  </svg>
  <div class="txt" style="left:30px;top:30px;width:42px;text-align:right"><b style="color:#333">Your Title Goes Here</b><br>Lorem ipsum dolor sit amet.</div>
  <div class="txt" style="left:20px;top:58px;width:42px;text-align:right"><b style="color:#333">Your Title Goes Here</b><br>Lorem ipsum dolor sit amet.</div>
  <div class="txt" style="left:140px;top:48px;width:46px"><b style="color:#333">Your Title Goes Here</b><br>Lorem ipsum dolor sit amet.</div>
  <div class="txt" style="left:132px;top:76px;width:46px"><b style="color:#333">Your Title Goes Here</b><br>Lorem ipsum dolor sit amet.</div>
  <div class="foot"><span>Confidential - Not for Distribution</span><span>www. corvixo-example.com</span></div>
</div>

<div class="slide" style="left:963px;top:904px">
  <div class="mark"></div><div class="logo">Corvixo</div>
  <div class="ttl" style="left:16px;top:25px">Your Title Text<br><span>Goes Here</span></div>
  <div class="txt" style="left:16px;top:46px;width:46px">Leverage agile frameworks to provide a robust synopsis for high level overviews.</div>
  <svg style="left:80px;top:30px" width="116" height="82" viewBox="0 0 116 82" font-family="Open Sans,sans-serif" font-size="7" font-weight="700" fill="#fff">
    <polygon points="2,70 30,58 36,68 8,80" fill="#f28c1c"/>
    <polygon points="26,54 54,42 60,52 32,64" fill="#f6a623"/>
    <polygon points="50,38 78,26 84,36 56,48" fill="#f28c1c"/>
    <polygon points="74,22 102,10 108,20 80,32" fill="#f6a623"/>
    <g transform="rotate(-23)"><text x="-12" y="75">01</text><text x="18" y="70">02</text><text x="48" y="64">03</text><text x="78" y="59">04</text></g>
  </svg>
  <div class="txt" style="left:130px;top:22px;width:34px;text-align:center"><b style="color:#333">Your Title</b><br>Lorem ipsum dolor.</div>
  <div class="txt" style="left:112px;top:42px;width:34px;text-align:center"><b style="color:#333">Your Title</b><br>Lorem ipsum dolor.</div>
  <div class="txt" style="left:92px;top:60px;width:34px;text-align:center"><b style="color:#333">Your Title</b><br>Lorem ipsum dolor.</div>
  <div class="txt" style="left:164px;top:80px;width:34px;text-align:center"><b style="color:#333">Option Here</b><br>Lorem ipsum dolor.</div>
  <div class="foot"><span>Confidential - Not for Distribution</span><span>www. corvixo-example.com</span></div>
</div>

<!-- row 8 -->
<div class="slide" style="left:31px;top:1050px">
  <div class="mark"></div><div class="logo">Corvixo</div>
  <div class="ttl c" style="top:23px">Your Title <span>Text Goes Here</span></div>
  <svg style="left:20px;top:40px" width="167" height="56" viewBox="0 0 167 56" font-family="Open Sans,sans-serif" font-size="2.4" fill="#555">
    <g font-weight="700" fill="#333"><text x="2" y="5">No</text><text x="14" y="5">Date</text><text x="45" y="5">Projects</text><text x="82" y="5">Status</text><text x="111" y="5">Value</text><text x="140" y="5">Location</text></g>
    <line x1="0" y1="7" x2="167" y2="7" stroke="#ddd" stroke-width=".4"/>
    <g><text x="2" y="14">01</text><text x="14" y="14">16 Feb 2020</text><text x="45" y="14">Blue projects</text><text x="82" y="14" fill="#f28c1c">80% progress</text><text x="111" y="14" fill="#f28c1c">$435.400,00</text><text x="140" y="14">London, UK</text></g>
    <line x1="0" y1="17" x2="167" y2="17" stroke="#eee" stroke-width=".4"/>
    <g><text x="2" y="23">02</text><text x="14" y="23">22 Mar 2020</text><text x="45" y="23">Red Grey projects</text><text x="82" y="23" fill="#f28c1c">45% progress</text><text x="111" y="23" fill="#f28c1c">$23.400,00</text><text x="140" y="23">Paris, FR</text></g>
    <rect x="0" y="27" width="167" height="7" fill="#f28c1c"/>
    <g fill="#fff"><text x="2" y="31.5">03</text><text x="14" y="31.5">22 Mar 2020</text><text x="45" y="31.5">Red Grey projects</text><text x="82" y="31.5">45% progress</text><text x="111" y="31.5">$23.400,00</text><text x="140" y="31.5">Paris, FR</text></g>
    <g><text x="2" y="41">04</text><text x="14" y="41">16 Feb 2020</text><text x="45" y="41">Blue projects</text><text x="82" y="41" fill="#f28c1c">80% progress</text><text x="111" y="41" fill="#f28c1c">$435.400,00</text><text x="140" y="41">London, UK</text></g>
    <line x1="0" y1="44" x2="167" y2="44" stroke="#eee" stroke-width=".4"/>
    <g><text x="2" y="50">05</text><text x="14" y="50">22 Mar 2020</text><text x="45" y="50">Red Grey projects</text><text x="82" y="50" fill="#f28c1c">45% progress</text><text x="111" y="50" fill="#f28c1c">$23.400,00</text><text x="140" y="50">Paris, FR</text></g>
  </svg>
  <div class="foot"><span>Confidential - Not for Distribution</span><span>www. corvixo-example.com</span></div>
</div>

<div class="slide" style="left:264px;top:1050px">
  <div class="mark"></div><div class="logo">Corvixo</div>
  <div class="ttl c" style="top:18px">Your Title <span>Text Goes Here</span></div>
  <svg style="left:12px;top:30px" width="183" height="58" viewBox="0 0 183 58" font-family="Open Sans,sans-serif" font-size="2.4" fill="#555" text-anchor="middle">
    <rect x="0" y="0" width="40" height="6" fill="#222"/><rect x="40" y="0" width="143" height="6" fill="#f28c1c"/>
    <g fill="#fff"><text x="20" y="4">Product Description</text><text x="56" y="4">ITEM01</text><text x="84" y="4">ITEM02</text><text x="112" y="4">ITEM03</text><text x="140" y="4">ITEM04</text><text x="168" y="4">ITEM05</text></g>
    <g><text x="20" y="11">Nullam quam quis</text><text x="56" y="11">$200</text><text x="84" y="11">$50</text><text x="112" y="11">$369</text><text x="140" y="11">$456</text><text x="168" y="11">$5000</text></g>
    <g><text x="20" y="17">Vestibulum in leo</text><text x="56" y="17">$5897</text><text x="84" y="17">$5412</text><text x="112" y="17">$2578</text><text x="140" y="17">$2978</text><text x="168" y="17">$125</text></g>
    <g><text x="20" y="23">Proin at felis in nis</text><text x="56" y="23">$697</text><text x="84" y="23">$892</text><text x="112" y="23">$7458</text><text x="140" y="23">$1235</text><text x="168" y="23">$4512</text></g>
    <g><text x="20" y="29">Nam molestie elit nec</text><text x="56" y="29">$102698</text><text x="84" y="29">$2103</text><text x="112" y="29">$365</text><text x="140" y="29">$5412</text><text x="168" y="29">$5412</text></g>
    <g><text x="20" y="35">Sed eu diam vestibulum</text><text x="56" y="35">$5980</text><text x="84" y="35">$50</text><text x="112" y="35">$50</text><text x="140" y="35">$478</text><text x="168" y="35">$54</text></g>
    <g><text x="20" y="41">Mauris consectetur</text><text x="56" y="41">$478980</text><text x="84" y="41">$5480</text><text x="112" y="41">$478</text><text x="140" y="41">$5412</text><text x="168" y="41">$5412</text></g>
    <rect x="0" y="44" width="40" height="6" fill="#222"/>
    <g><text x="20" y="48" fill="#fff">Grand Total</text><text x="56" y="48">$1510932</text><text x="84" y="48">$13987</text><text x="112" y="48">$14509</text><text x="140" y="48">$18973</text><text x="168" y="48">$20515</text></g>
  </svg>
  <div class="txt" style="left:30px;right:30px;top:88px;text-align:center">Lorem ipsum dolor sit amet, consectetur adipiscing elit. Aenean commodo ligula eget dolor.</div>
  <div class="foot"><span>Confidential - Not for Distribution</span><span>www. corvixo-example.com</span></div>
</div>

<div class="slide" style="left:497px;top:1050px">
  <div class="mark"></div><div class="logo">Corvixo</div>
  <div class="card" style="left:16px;top:22px;width:82px;height:76px"></div>
  <div class="ttl" style="left:26px;top:34px">Your Title Text<br>Goes Here</div>
  <div class="txt" style="left:26px;top:55px;width:64px">Lorem ipsum dolor sit amet, consectetuer adipiscing elit.</div>
  <div class="dot orng" style="left:30px;top:74px;width:9px;height:9px"></div>
  <div class="dot" style="left:46px;top:74px;width:9px;height:9px;background:var(--amber)"></div>
  <div class="dot" style="left:62px;top:74px;width:9px;height:9px;background:#c0603a"></div>
  <svg style="left:100px;top:28px" width="100" height="72" viewBox="0 0 100 72" font-family="Open Sans,sans-serif" font-size="2.4" fill="#888">
    <rect x="64" y="0" width="34" height="5" fill="#f28c1c"/><text x="81" y="3.5" fill="#fff" text-anchor="middle">2022 Data Report</text>
    <g stroke="#eee" stroke-width=".4"><line x1="12" y1="10" x2="98" y2="10"/><line x1="12" y1="22" x2="98" y2="22"/><line x1="12" y1="34" x2="98" y2="34"/><line x1="12" y1="46" x2="98" y2="46"/><line x1="12" y1="58" x2="98" y2="58"/></g>
    <text x="2" y="11">350</text><text x="2" y="23">250</text><text x="2" y="35">150</text><text x="2" y="47">100</text><text x="2" y="59">0</text>
    <path d="M12 58 L20 46 L28 50 L36 40 L44 44 L52 34 L60 40 L68 28 L76 36 L84 22 L92 32 L98 26 L98 58 Z" fill="#f6a623"/>
    <path d="M12 58 L20 52 L28 54 L36 48 L44 52 L52 44 L60 48 L68 40 L76 46 L84 36 L92 44 L98 40 L98 58 Z" fill="#f28c1c"/>
    <g><text x="14" y="65">Jan</text><text x="22" y="65">Feb</text><text x="30" y="65">Mar</text><text x="38" y="65">Apr</text><text x="46" y="65">May</text><text x="54" y="65">Jun</text><text x="62" y="65">Jul</text><text x="70" y="65">Aug</text><text x="78" y="65">Sep</text><text x="86" y="65">Oct</text><text x="94" y="65">Nov</text></g>
  </svg>
  <div class="foot"><span>Confidential - Not for Distribution</span><span>www. corvixo-example.com</span></div>
</div>

<div class="slide" style="left:729px;top:1050px">
  <div class="mark"></div><div class="logo">Corvixo</div>
  <div class="ic" style="left:20px;top:24px;margin:0"></div>
  <div class="txt" style="left:20px;top:36px;width:48px"><b style="color:var(--orange)">Report Feature 1</b><br>A wonderful serenity has taken possession of my entire soul.</div>
  <div class="ic" style="left:20px;top:60px;margin:0"></div>
  <div class="txt" style="left:20px;top:72px;width:48px"><b style="color:var(--orange)">Report Feature 2</b><br>A wonderful serenity has taken possession of my entire soul.</div>
  <div class="card" style="left:88px;top:20px;width:50px;height:80px;text-align:left;padding:4px"><div class="big" style="font-size:6px">2021</div><div class="txt">Sed ut perspiciatis</div></div>
  <div class="card" style="left:142px;top:20px;width:50px;height:80px;text-align:left;padding:4px"><div class="big" style="font-size:6px">2022</div><div class="txt">Sed ut perspiciatis</div></div>
  <svg style="left:92px;top:48px" width="96" height="46" viewBox="0 0 96 46">
    <g fill="#f28c1c"><rect x="4" y="14" width="2" height="28"/><rect x="9" y="22" width="2" height="20"/><rect x="14" y="8" width="2" height="34"/><rect x="19" y="26" width="2" height="16"/><rect x="24" y="18" width="2" height="24"/><rect x="29" y="4" width="2" height="38"/><rect x="34" y="20" width="2" height="22"/></g>
    <g fill="#d99a1a"><rect x="58" y="22" width="2" height="20"/><rect x="63" y="12" width="2" height="30"/><rect x="68" y="26" width="2" height="16"/><rect x="73" y="6" width="2" height="36"/><rect x="78" y="18" width="2" height="24"/><rect x="83" y="10" width="2" height="32"/><rect x="88" y="24" width="2" height="18"/></g>
  </svg>
  <div class="foot"><span>Confidential - Not for Distribution</span><span>www. corvixo-example.com</span></div>
</div>

<div class="slide" style="left:963px;top:1050px">
  <div class="mark"></div><div class="logo">Corvixo</div>
  <div class="ttl" style="left:17px;top:26px">Your Title Text<br><span>Goes Here</span></div>
  <div class="txt" style="left:17px;top:51px;width:80px">Lorem ipsum dolor sit amet, consectetuer adipiscing elit.</div>
  <div class="row" style="left:20px;top:62px;width:78px;justify-content:space-around"><span class="big" style="font-size:5px">70,5%</span><span class="big" style="font-size:5px">80,5%</span></div>
  <div class="row" style="left:20px;top:80px;width:78px;justify-content:space-around"><span class="big" style="font-size:5px">80,5%</span><span class="big" style="font-size:5px">90,0%</span></div>
  <svg style="left:108px;top:28px" width="80" height="76" viewBox="0 0 80 76" font-family="Open Sans,sans-serif" font-size="3" fill="#fff" text-anchor="middle">
    <g transform="translate(44 36) rotate(-90)">
      <circle r="15" fill="none" stroke="#e06a10" stroke-width="30" stroke-dasharray="54.66 94.25"/>
      <circle r="15" fill="none" stroke="#f6a623" stroke-width="30" stroke-dasharray="21.68 94.25" stroke-dashoffset="-54.66"/>
      <circle r="15" fill="none" stroke="#f28c1c" stroke-width="30" stroke-dasharray="9.43 94.25" stroke-dashoffset="-76.34"/>
      <circle r="15" fill="none" stroke="#f7c14a" stroke-width="30" stroke-dasharray="8.48 94.25" stroke-dashoffset="-85.77"/>
    </g>
    <text x="62" y="38">58%</text><text x="26" y="46">23%</text><text x="28" y="22">10%</text><text x="40" y="16">9%</text>
    <g fill="#888" text-anchor="start" font-size="2.4"><text x="4" y="72">■2017  ■2018  ■2019  ■2020</text></g>
  </svg>
  <div class="foot"><span>Confidential - Not for Distribution</span><span>www. corvixo-example.com</span></div>
</div>

</div>
</body>
</html>
```